Tidewell Gin - Label for new Gin bottle

I am looking for a bottle label for our small batch, handcrafted Gin. We are located in the bay-side city of Frankston (Victoria, Australia). I know I want more of a serious label but am torn between traditional or modern styling.

Label to include;
• Tidewell GIN (name)
• Hand Crafted
• Small Batch
• 40% Vol

Using 700ml MERIDA Spirit Bottle - Cork

Requirements
Must have
• Name; Tidewell Gin
Method: Hand Crafted
Batch Size; Small Batch
Alc; 40% Vol
Nice to have
• Maybe a coastal/seaside reference or reference to distilling.

```html
<!DOCTYPE html>
<html lang="en">
<head>
<meta charset="utf-8">
<title>Tidewell Gin – Bottle Label</title>
<link rel="stylesheet" href="https://fonts.googleapis.com/css2?family=Cinzel:wght@700&family=Arvo:wght@700&family=Libre+Baskerville:wght@400;700&display=swap">
<style>
  :root {
    --page: #ffffff;
    --ink: #1c1c1c;
    --sky-top: #f6c6b4;
    --sky-mid: #f9ece2;
    --sky-low: #f8f3ea;
    --sea-top: #a9c8ea;
    --sea-mid: #e2ebf6;
    --sea-low: #f0f4fb;
    --brand-teal: #1f8f96;
    --gin-red: #e51b23;
    --craft-blue: #3c3f9c;
    --craft-edge: #d52a35;
    --scene-dark: #3a3a3a;
    --scene-light: #c7d0dc;
  }
  html, body {
    margin: 0;
    padding: 0;
    width: 907px;
    height: 1200px;
    overflow: hidden;
    background: var(--page);
  }
  .canvas {
    position: relative;
    width: 907px;
    height: 1200px;
  }
  .label {
    position: absolute;
    left: 0;
    top: 0;
    width: 907px;
    height: 1200px;
  }
  .brand-name {
    font-family: "Cinzel", serif;
    font-weight: 700;
    font-size: 82px;
    fill: var(--brand-teal);
  }
  .gin-word {
    font-family: "Arvo", serif;
    font-weight: 700;
    font-size: 84px;
    fill: var(--gin-red);
  }
  .method {
    font-family: "Arvo", serif;
    font-weight: 700;
    font-size: 39px;
    fill: var(--craft-blue);
    stroke: var(--craft-edge);
    stroke-width: 1.2px;
    paint-order: stroke;
  }
  .batch {
    font-family: "Libre Baskerville", serif;
    font-weight: 700;
    font-size: 17px;
    fill: var(--ink);
  }
  .strength {
    font-family: "Libre Baskerville", serif;
    font-weight: 700;
    font-size: 24px;
    fill: var(--ink);
  }
</style>
</head>
<body>
<main class="canvas">
  <svg class="label" viewBox="0 0 907 1200" xmlns="http://www.w3.org/2000/svg">
    <defs>
      <linearGradient id="sky" x1="0" y1="0" x2="0" y2="1">
        <stop offset="0" stop-color="var(--sky-top)"/>
        <stop offset="0.5" stop-color="var(--sky-mid)"/>
        <stop offset="1" stop-color="var(--sky-low)"/>
      </linearGradient>
      <linearGradient id="sea" x1="0" y1="0" x2="0" y2="1">
        <stop offset="0" stop-color="var(--sea-top)"/>
        <stop offset="0.25" stop-color="var(--sea-mid)"/>
        <stop offset="1" stop-color="var(--sea-low)"/>
      </linearGradient>
      <linearGradient id="scene-tone" x1="0" y1="0" x2="0" y2="1">
        <stop offset="0" stop-color="var(--scene-dark)" stop-opacity="0.45"/>
        <stop offset="0.5" stop-color="var(--scene-dark)" stop-opacity="0.35"/>
        <stop offset="1" stop-color="var(--scene-light)" stop-opacity="0.3"/>
      </linearGradient>
      <clipPath id="oval-clip">
        <ellipse cx="453.5" cy="600" rx="428" ry="305"/>
      </clipPath>
    </defs>

    <g class="label-field" clip-path="url(#oval-clip)">
      <rect class="sky-band" x="0" y="290" width="907" height="316" fill="url(#sky)"/>
      <rect class="sea-band" x="0" y="606" width="907" height="310" fill="url(#sea)"/>
    </g>

    <rect class="shore-scene" x="112" y="440" width="128" height="320" rx="6"
          fill="url(#scene-tone)" role="img"
          aria-label="Silhouette of palm trees, a beach gazebo with sun loungers and a small jetty, reflected in calm water"/>

    <ellipse class="label-border" cx="453.5" cy="600" rx="428" ry="305" fill="none" stroke="var(--ink)" stroke-width="4"/>
    <ellipse class="label-inner-rule" cx="453.5" cy="600" rx="418" ry="295" fill="none" stroke="var(--ink)" stroke-width="0.8"/>

    <text class="brand-name" x="466" y="512" text-anchor="middle">TIDEWELL</text>
    <text class="gin-word" x="458" y="604" text-anchor="middle">GIN</text>
    <text class="method" x="458" y="772" text-anchor="middle">HAND CRAFTED</text>
    <text class="batch" x="460" y="811" text-anchor="middle">SMALL BATCH</text>
    <text class="strength" x="460" y="863" text-anchor="middle">40% VOL</text>
  </svg>
</main>
</body>
</html>
```